The Brightwater Compass Business Card

We need an attractive business card with the logo that we bought from ArtVantly last year.
Our mission is to contribute to change the way today's leaders manage business companies bringing value to the workplace and helping them to build a new model of creating wealth.
Our logo is clear about our values : we seek Positive Change through People and are convinced that the pursuit of individual well-being and the chase of economic results can converge with the right management.
Management Consulting
Corinne Fabrelle
+34 612 98 70 31
corinne.fabrelle@thebrightwatercompass-mail.net
www.thebrightwatercompass-mail.net

```html
<!DOCTYPE html>
<html lang="en">
<head>
<meta charset="utf-8">
<title>The Brightwater Compass – Business Card</title>
<link rel="stylesheet" href="https://fonts.googleapis.com/css2?family=Roboto+Slab:wght@400;600;700&display=swap">
<style>
  :root {
    --backdrop: #9d8e8e;
    --teal-deep: #0e7673;
    --teal-mid: #13948f;
    --teal-light: #8fd3cf;
    --card-white: #ffffff;
    --arc-grey: #eef0f0;
    --ink: #1c1c1c;
    --line-white: rgba(255,255,255,0.85);
  }
  * { box-sizing: border-box; margin: 0; padding: 0; }
  html, body {
    width: 1200px; height: 1000px; overflow: hidden;
    background: var(--backdrop);
    font-family: "Roboto Slab", Georgia, serif;
  }
  .canvas { position: relative; width: 1200px; height: 1000px; }

  .card {
    position: absolute;
    width: 560px; height: 320px;
    border-radius: 24px;
    overflow: hidden;
    box-shadow: 0 14px 30px rgba(0,0,0,0.22);
  }

  /* Back side */
  .card-back {
    left: 80px; top: 130px;
    background: radial-gradient(circle at 65% 70%, var(--teal-mid), var(--teal-deep) 75%);
  }
  .card-back .brand {
    position: absolute; left: 46px; top: 92px;
    display: flex; align-items: center; gap: 12px;
  }
  .brand-dot {
    width: 22px; height: 22px; border-radius: 50%;
    background: currentColor; flex: none;
  }
  .brand-name {
    font-size: 25px; font-weight: 600; letter-spacing: 0.5px;
    white-space: nowrap;
  }
  .card-back .brand { color: var(--card-white); }
  .card-back .speed-lines { position: absolute; inset: 0; }
  .card-back .web {
    position: absolute; right: 28px; bottom: 92px;
    color: var(--card-white); font-size: 14px; font-weight: 700;
  }

  /* Front side */
  .card-front {
    left: 560px; top: 540px;
    background: var(--card-white);
  }
  .card-front .decor { position: absolute; inset: 0; }
  .card-front .brand {
    position: absolute; right: 104px; top: 48px;
    color: var(--teal-deep);
    display: flex; align-items: center; gap: 10px;
  }
  .card-front .brand-name { font-size: 21px; }
  .card-front .brand-dot { width: 18px; height: 18px; }
  .side-bar {
    position: absolute; right: 32px; top: 112px;
    width: 56px; height: 150px;
    background: var(--teal-deep);
  }
  .holder {
    position: absolute; right: 104px; top: 118px;
    text-align: right;
  }
  .holder-name {
    color: var(--teal-deep);
    font-size: 28px; font-weight: 700;
    padding-bottom: 6px;
    border-bottom: 2px solid var(--teal-deep);
  }
  .contact-list {
    position: absolute; right: 104px; top: 180px;
    list-style: none; text-align: right;
    color: var(--ink); font-size: 14px; font-weight: 700; line-height: 22px;
  }
  .contact-list .gap { margin-top: 20px; }
</style>
</head>
<body>
<main class="canvas">

  <section class="card card-back" aria-label="Card back">
    <svg class="speed-lines" width="560" height="320" viewBox="0 0 560 320" aria-hidden="true">
      <g stroke="var(--line-white)" stroke-width="1.4" fill="none">
        <line x1="560" y1="95" x2="300" y2="200"/>
        <line x1="560" y1="108" x2="270" y2="222"/>
        <line x1="560" y1="121" x2="240" y2="244"/>
        <line x1="560" y1="134" x2="200" y2="268"/>
        <line x1="560" y1="147" x2="0" y2="320"/>
      </g>
    </svg>
    <div class="brand">
      <span class="brand-dot"></span>
      <span class="brand-name">The Brightwater Compass</span>
    </div>
    <p class="web">www.thebrightwatercompass-mail.net</p>
  </section>

  <section class="card card-front" aria-label="Card front">
    <svg class="decor" width="560" height="320" viewBox="0 0 560 320" aria-hidden="true">
      <path d="M250 0 C 130 60, 110 220, 150 320 L 195 320 C 160 220, 180 80, 290 0 Z" fill="var(--arc-grey)"/>
      <line x1="0" y1="250" x2="470" y2="150" stroke="var(--teal-light)" stroke-width="2"/>
    </svg>
    <div class="brand">
      <span class="brand-dot"></span>
      <span class="brand-name">The Brightwater Compass</span>
    </div>
    <div class="side-bar"></div>
    <div class="holder">
      <p class="holder-name">Corinne Fabrelle</p>
    </div>
    <ul class="contact-list">
      <li>+34 612 98 70 31</li>
      <li class="gap">www.thebrightwatercompass-mail.net</li>
      <li>corinne.fabrelle@thebrightwatercompass-mail.net</li>
    </ul>
  </section>

</main>
</body>
</html>
```